PDF to help promote my website to potential advertisers

I need a one page PDF that may be used on our site to help promote my website (LVRnests.com) to potential advertisers. It's a pretty simple document but needs to make it look great.

I've provided the audience info. I'm hoping to have this look sorta like the Ledger Quarter's advertising page: http://www.ledgerquarter.example/advertise

It's not rocket science but I hope you can help.

Target Market(s)

Potential Advertisers are typically home improvement-related-services like contractors and home builders. Also real estate agents and home-sales related services.

Industry/Entity Type

Media

Colors

Designer to choose colors to be used in the design.

Requirements
Must have
• I want the graphics to make the audience info (in the txt file) stand out. Needs to be similar to this: http://www.ledgerquarter.example/advertise.
• I want to use the PDF to send via email to prospective clients and also post on our website, so it has to be able to work almost like graphics on a site. I may have it printed as well.
Nice to have
• Colors and logo and font should match our site. Please grab the logo and/font info from our site

```html
<!DOCTYPE html>
<html lang="en">
<head>
<meta charset="utf-8">
<title>Advertising with LVRnests</title>
<link href="https://fonts.googleapis.com/css2?family=Exo+2:wght@200;300;400;700;800;900&family=Lato:wght@400;700&display=swap" rel="stylesheet">
<style>
  :root {
    --page: #eef0f2;
    --sky-top: #2c3f5c;
    --sky-mid: #3d5169;
    --haze: #6b7a72;
    --grass: #4f7d2c;
    --grass-deep: #3c6321;
    --white: #ffffff;
    --ink: #161616;
    --cyan: #1fb1e6;
    --orange: #f07a22;
    --navy-text: #0f2a44;
  }
  * { margin: 0; padding: 0; box-sizing: border-box; }
  html, body { width: 1200px; height: 1200px; overflow: hidden; background: var(--page); }
  .flyer {
    position: absolute; left: 194px; top: 40px;
    width: 812px; height: 1120px; overflow: hidden;
    font-family: "Exo 2", sans-serif; color: var(--white);
  }
  .flyer__photo {
    position: absolute; inset: 0;
    background:
      radial-gradient(ellipse 45% 30% at 50% 45%, rgba(190,120,90,0.35), transparent 70%),
      linear-gradient(180deg, var(--sky-top) 0%, var(--sky-mid) 38%, var(--haze) 58%, var(--grass) 72%, var(--grass-deep) 100%);
  }
  .brand {
    position: absolute; top: 72px; left: 0; width: 100%;
    display: flex; justify-content: center; align-items: center; gap: 12px;
  }
  .brand__mark { width: 40px; height: 40px; background: var(--cyan); }
  .brand__name { font-size: 42px; font-weight: 700; color: var(--white); }
  .headline { position: absolute; left: 0; width: 100%; text-align: center; }
  .headline--advertising {
    top: 180px; font-size: 114px; font-weight: 800; letter-spacing: 1px; line-height: 1;
  }
  .headline--with { top: 322px; font-size: 48px; font-weight: 300; line-height: 1; }
  .headline--brand { top: 378px; font-size: 158px; line-height: 1; letter-spacing: -2px; }
  .headline--brand .thin { font-weight: 200; }
  .headline--brand .heavy { font-weight: 900; }
  .pitch { position: absolute; left: 60px; width: 700px; text-align: center; font-weight: 300; }
  .pitch--lead { top: 560px; font-size: 33px; }
  .pitch--audience {
    top: 606px; height: 66px; background: var(--white); color: var(--ink);
    font-size: 60px; font-weight: 800; line-height: 66px; letter-spacing: 0.5px;
  }
  .pitch--follow { top: 676px; font-size: 33px; }
  .about {
    position: absolute; top: 837px; left: 54px; width: 706px; height: 101px;
    font-family: "Lato", sans-serif;
  }
  .about__tag {
    position: absolute; left: 0; top: 0; width: 170px; height: 101px;
  }
  .about__tag-text {
    position: absolute; left: 0; top: 0; width: 150px; height: 101px;
    display: flex; flex-direction: column; justify-content: center; align-items: center;
    color: var(--navy-text); font-size: 15px; line-height: 1.3;
  }
  .about__tag-text strong { font-weight: 700; }
  .about__stats {
    position: absolute; left: 172px; top: 6px; width: 526px;
    font-size: 11.6px; line-height: 1.55; color: var(--white); text-align: justify;
  }
  .about__stats b { font-size: 14px; }
  .contact {
    position: absolute; top: 1064px; left: 0; width: 100%;
    display: flex; justify-content: center; gap: 28px;
    font-family: "Lato", sans-serif; font-size: 13px; color: var(--white);
  }
  .contact__item { display: flex; align-items: center; gap: 7px; }
  .contact__item--phone { font-weight: 700; font-size: 15px; }
  .contact__dot { width: 11px; height: 11px; border-radius: 50%; background: var(--cyan); }
</style>
</head>
<body>
  <main class="flyer">
    <div class="flyer__photo" role="img" aria-label="Photo of a small model house held in open hands above a green lawn under a dark blue sky"></div>

    <div class="brand">
      <span class="brand__mark"></span>
      <span class="brand__name">LVRnests</span>
    </div>

    <h1 class="headline headline--advertising">ADVERTISING</h1>
    <p class="headline headline--with">with</p>
    <p class="headline headline--brand"><span class="thin">LVR</span><span class="heavy">NESTS</span></p>

    <p class="pitch pitch--lead">Learn how you can partner with us to reach our</p>
    <p class="pitch pitch--audience">MILWAUKEE AUDIENCE</p>
    <p class="pitch pitch--follow">who desire to move and/or renovate their homes</p>

    <section class="about">
      <svg class="about__tag" viewBox="0 0 170 101" aria-hidden="true">
        <rect x="0" y="0" width="706" height="101" fill="var(--orange)"/>
        <polygon points="0,0 150,0 165,50.5 150,101 0,101" fill="var(--cyan)"/>
        <polygon points="150,0 156,0 171,50.5 156,101 150,101 165,50.5" fill="var(--white)"/>
      </svg>
      <div style="position:absolute;left:170px;top:0;width:536px;height:101px;background:var(--orange);"></div>
      <div class="about__tag-text"><span>About</span><strong>LVRnests.com:</strong></div>
      <p class="about__stats">We reach over <b>1000</b> readers each day through our website, our Porchlight Page, our Snapframe and our email newsletter. <b>67%</b> are women <b>55%</b> in the prime home purchase age range of <b>25-44</b> <b>75%</b> in milwaukee area <b>60%</b> claim they are <b>"happy but looking"</b> for a future new home <b>55%</b> plan to do a home improvement projects in the next year <b>30%</b> do not have an agent.</p>
    </section>

    <footer class="contact">
      <span class="contact__item contact__item--phone">
        <svg width="14" height="14" viewBox="0 0 24 24" aria-hidden="true"><path fill="var(--cyan)" d="M6.6 10.8c1.4 2.8 3.8 5.1 6.6 6.6l2.2-2.2c.3-.3.7-.4 1-.2 1.1.4 2.3.6 3.6.6.6 0 1 .4 1 1V20c0 .6-.4 1-1 1C10.6 21 3 13.4 3 4c0-.6.4-1 1-1h3.5c.6 0 1 .4 1 1 0 1.3.2 2.5.6 3.6.1.3 0 .7-.2 1z"/></svg>
        +1 555-014-2290
      </span>
      <span class="contact__item">
        <svg width="14" height="14" viewBox="0 0 24 24" aria-hidden="true"><rect x="2" y="5" width="20" height="14" rx="2" fill="var(--cyan)"/><path d="M2 6l10 7 10-7" stroke="var(--white)" stroke-width="1.6" fill="none"/></svg>
        info@lvrnests.example
      </span>
      <span class="contact__item"><span class="contact__dot"></span>www.lvrnests.com</span>
      <span class="contact__item"><span class="contact__dot"></span>/LVRnests</span>
      <span class="contact__item"><span class="contact__dot"></span>/LVRnests</span>
    </footer>
  </main>
</body>
</html>
```